Tactical Supply Company needing memorable business card design

Our tactical supply comapny is in need of a new business card design that will set us apart from the amateurs. We sell tactical gear ranging from backpacks and range bags to apparel and other gear. We are looking for a sharp design that incorporates our logo, website, and name. Our colors are white, red, and black, or any combination of the three, preferably red and black.
I have attached our logo with our name underneath but I have also edited that design with the logo incorporated next to the name (attached).

Target Market(s)

Law enforcement, military, tactical

Industry/Entity Type

Business

Contact Information for Business Card

Include www.fernhollowprovisions-demo.com

Colors
000000
ec1f27
ffffff

Requirements
Must have
• Our name, logo, and website. This is intended to be a memorable simple card, no name, address, email, or phone number info is necessary. Designs that do include this additional info will still be considered if they are absolutely spectacular.
Should not have
• A standard template design, I can create that in my own on Cardvellum. I am looking for a new, creative design that is completely unique to my company.

```html
<!DOCTYPE html>
<html lang="en">
<head>
<meta charset="utf-8">
<title>Fern Hollow Provisions – Business Card</title>
<link rel="stylesheet" href="https://fonts.googleapis.com/css2?family=Montserrat:wght@400;500;700;800&display=swap">
<style>
  :root {
    --red: #ec1f27;
    --black: #000000;
    --white: #ffffff;
    --ink: #2a2a2a;
    --card-front: #f3f3f3;
    --card-back: #333132;
    --stage-top: #a9a9a9;
    --stage-bottom: #ececec;
  }
  * { box-sizing: border-box; margin: 0; padding: 0; }
  html, body { width: 1200px; height: 853px; overflow: hidden; }
  body {
    position: relative;
    background: linear-gradient(to bottom, var(--stage-top) 0%, #c4c4c4 48%, var(--stage-bottom) 60%, var(--stage-bottom) 100%);
    font-family: "Montserrat", sans-serif;
  }
  .card {
    position: absolute;
    top: 307px;
    width: 423px;
    height: 241px;
    box-shadow: 0 2px 6px rgba(0,0,0,0.18);
  }
  .card-front { left: 130px; background: var(--card-front); }
  .card-back { left: 622px; background: var(--card-back); }

  .name-tag {
    position: absolute;
    top: 41px; right: 0;
    width: 167px; height: 49px;
    background: var(--red);
    border-radius: 3px 0 0 3px;
    color: var(--white);
    padding: 9px 0 0 13px;
  }
  .name-tag .person { font-size: 15px; letter-spacing: 0.3px; line-height: 1; }
  .name-tag .person b { font-weight: 800; }
  .name-tag .person span { font-weight: 400; }
  .name-tag .role { font-size: 7.5px; font-weight: 700; margin: 4px 0 0 11px; letter-spacing: 0.3px; }
  .name-tag .bar {
    position: absolute; right: 38px; top: 10px;
    width: 3px; height: 29px; background: var(--black); border-radius: 2px;
  }

  .brand {
    position: absolute; left: 32px; top: 184px;
    display: flex; align-items: center; gap: 6px;
  }
  .brand .mark { width: 10px; height: 10px; background: var(--red); }
  .brand .wordmark {
    font-size: 14px; font-weight: 800; color: var(--black);
    letter-spacing: 0.2px; line-height: 1;
  }

  .contact {
    position: absolute; right: 40px; top: 137px;
    text-align: right; color: var(--ink);
    font-size: 10.5px; line-height: 13px; font-weight: 500;
  }
  .contact .rule { width: 16px; height: 2px; background: var(--red); margin: 6px 0 10px auto; }
  .contact-lines {
    position: absolute; right: 9px; top: 183px;
    font-size: 10.5px; line-height: 14px; color: var(--ink); font-weight: 500;
  }
  .contact-lines li { list-style: none; display: flex; justify-content: flex-end; align-items: center; gap: 6px; }
  .contact-lines svg { width: 10px; height: 9px; fill: var(--ink); }

  .back-brand {
    position: absolute; left: 0; right: 0; top: 108px;
    display: flex; justify-content: center; align-items: center; gap: 9px;
  }
  .back-brand .mark { width: 14px; height: 14px; background: var(--red); }
  .back-brand .wordmark { font-size: 19px; font-weight: 800; color: var(--white); letter-spacing: 0.4px; }
</style>
</head>
<body>
  <section class="card card-front">
    <div class="name-tag">
      <p class="person"><b>DALE</b> <span>MARSH</span></p>
      <p class="role">FOUNDER &amp; CEO</p>
      <div class="bar"></div>
    </div>

    <div class="brand">
      <div class="mark"></div>
      <p class="wordmark">FERN HOLLOW</p>
    </div>

    <div class="contact">
      <p>Millbrook,<br>Oregon 97031</p>
      <div class="rule"></div>
    </div>
    <ul class="contact-lines">
      <li>555 014 2290
        <svg viewBox="0 0 10 9"><path d="M1 3 Q5 0 9 3 L8 4 L6.5 3.2 L6.5 4.3 L8.5 6 V8.5 H1.5 V6 L3.5 4.3 L3.5 3.2 L2 4 Z"/></svg></li>
      <li>desk@fernhollow-demo.com
        <svg viewBox="0 0 10 9"><path d="M0.5 1.5 H9.5 V7.5 H0.5 Z M1.2 2.2 L5 5 L8.8 2.2 Z" fill-rule="evenodd"/></svg></li>
      <li>www.fernhollowprovisions-demo.com
        <svg viewBox="0 0 10 9"><path d="M0.5 0.5 H9.5 V6.5 H6 V7.5 H7.5 V8.5 H2.5 V7.5 H4 V6.5 H0.5 Z M1.5 1.5 V5.5 H8.5 V1.5 Z" fill-rule="evenodd"/></svg></li>
    </ul>
  </section>

  <section class="card card-back">
    <div class="back-brand">
      <div class="mark"></div>
      <p class="wordmark">FERN HOLLOW</p>
    </div>
  </section>
</body>
</html>
```